Litigation services brochure for TRV.law

improve aesthetics and sync with website color scheme and new staff to emphasize law firm's litigation capabilities. Describe Litigation director, senior attorneys, attorneys, and general capabilities of the firm, licenses to practice, representative trasnactions and litigation experience. Take profile info from individual attorneys listed in the .doc and correlate with www.trv.law profiles for same attorneys. Update photos as needed. I'm not sure what other words I need to add, but this thing says there needs to be more words in my project description. read the brochure attached, and it should be pretty self explanatory. We have lots of info and content on there, we just want it to look better and reflect the updated color scheme of the site (a few of the color bar colors have changed order and color).

Target Market(s)

Houston, Denver

Font styles to use
Serif

Requirements
Must have
• Color scheme that matches www.trv.law
Nice to have
• Better aesthetics and content optimization

```html
<!DOCTYPE html>
<html lang="en">
<head>
<meta charset="utf-8">
<title>TRV.law Litigation Brochure</title>
<link href="https://fonts.googleapis.com/css2?family=Libre+Baskerville&family=Source+Sans+3:wght@400;600;700&display=swap" rel="stylesheet">
<style>
:root{
  --backdrop:#2c2c2e;
  --paper:#ffffff;
  --ink:#231f20;
  --muted:#3a3a3a;
  --tan:#c9b27b;
  --forest:#0e3a1f;
  --gold:#f2b21c;
  --orange:#e8731e;
  --maroon:#8e1a44;
  --navy:#1f2a6b;
  --photo-a:#6d5a4a;
  --photo-b:#2b2a2c;
}
*{margin:0;padding:0;box-sizing:border-box}
html,body{width:1200px;height:843px;overflow:hidden;background:var(--backdrop)}
body{position:relative;font-family:"Source Sans 3",Arial,sans-serif;color:var(--ink)}
.page{position:absolute;left:49px;top:65px;width:1102px;height:713px;background:var(--paper)}
.abs{position:absolute}
.firm-name{left:51px;top:26px;font-family:"Libre Baskerville",Georgia,serif;font-variant:small-caps;font-size:21px;letter-spacing:.5px;color:#3b3b3b}
.firm-web{right:37px;top:32px;font-family:"Libre Baskerville",Georgia,serif;font-size:10px;letter-spacing:.5px;color:#222}
.color-bar{left:0;top:51px;width:1102px;height:4px;display:flex}
.color-bar span{height:100%}
.photo{background:linear-gradient(160deg,var(--photo-a),var(--photo-b))}
.name{font-weight:700;color:var(--orange);font-size:17px;line-height:1}
.role{font-size:11px;line-height:1;margin-top:5px}
.contact{font-size:11px;display:flex;align-items:center;gap:4px;margin-top:7px;white-space:nowrap}
.contact svg{width:10px;height:9px;flex:none}
.contact .gap{width:14px}
.bio{font-size:8.1px;line-height:11.9px;text-align:justify;color:var(--muted)}
.bio p+p{margin-top:12px}
.adm-title{font-weight:700;font-size:11px;line-height:1}
.adm-list{list-style:none;font-weight:700;font-size:8px;line-height:11.5px;margin:4px 0 0 8px}
.page-num{left:0;top:653px;width:38px;height:31px;background:var(--navy);color:#fff;font-size:12px;display:flex;align-items:center;justify-content:center}
.feature{left:551px;top:364px;width:551px;height:298px;background:var(--forest);color:#fff}
.feature .name{color:#fff;font-size:17px}
.feature .bio{color:#fff}
.feature .adm-title,.feature .adm-list{color:#fff}
.mail-icon-row{margin-top:3px;line-height:0}
.mail-icon-row svg{width:10px;height:9px}
</style>
</head>
<body>
<div class="page">
  <div class="abs firm-name">Thornton Reyes &amp; Vance</div>
  <div class="abs firm-web">WWW.TRV.LAW</div>
  <div class="abs color-bar">
    <span style="width:413px;background:var(--tan)"></span>
    <span style="width:171px;background:var(--forest)"></span>
    <span style="width:172px;background:var(--gold)"></span>
    <span style="width:173px;background:var(--orange)"></span>
    <span style="width:173px;background:var(--maroon)"></span>
  </div>

  <div class="abs photo" role="img" aria-label="Portrait of Martin L. Greer in suit before bookshelves" style="left:66px;top:154px;width:173px;height:168px"></div>
  <div class="abs" style="left:255px;top:274px">
    <div class="name">Martin L. Greer</div>
    <div class="role">J.D., Senior Attorney, Business &amp; Litigation</div>
    <div class="contact">
      <svg viewBox="0 0 10 9"><rect x="0" y="0" width="10" height="9" rx="1" fill="var(--orange)"/><path d="M1 2l4 3 4-3" stroke="#fff" fill="none" stroke-width="1"/></svg>
      <span>mgreer@trv.law</span><span class="gap"></span>
      <svg viewBox="0 0 10 9"><path d="M1 3c0-2 8-2 8 0v1H7V3H3v1H1z M2 5h6l1 4H1z" fill="var(--orange)"/></svg>
      <span>(713) 555-0142</span>
    </div>
  </div>
  <div class="abs bio" style="left:66px;top:342px;width:435px">
    <p>Martin L. Greer is a Senior Attorney with Thornton, Reyes &amp; Vance, PLLC. Martin's practice focuses on the areas of international business law, general business representation, corporate law, commercial litigation, and intellectual property law. In addition, Mr. Greer counsels clients regarding a variety of business transactions, from basic entity formation to complex cross-border acquisitions or licensing agreements. Martin has advised business clients on legal matters involving Canada, Mexico, Italy, Germany, Britain, Ireland, France, Belgium, Netherlands, Luxembourg, Sweden, Malta, Russia, Central African Republic, Ghana, Saudi Arabia, India, Malaysia, Singapore, South Korea, and the United States. As an arbitrator, Mr. Greer is available for appointment as arbitrator for commercial, international, securities, and intellectual property cases. Martin is a member of numerous arbitration rosters including Commercial, International, Chamber and Securities panels, the Continental Arbitration Tribunal, and the City of Houston. Mr. Greer has represented clients with pro hac vice appearances in Florida, Michigan and Montana, as well as United States District Courts for the Central District of California, District of Maryland, District of Utah, District of Wyoming, Southern District of Florida, and Eastern District of North Carolina.</p>
    <p>Martin completed his J.D. from Bayou City University, cum laude, where he served as student body vice-president. Prior to law school, Martin attended Capitol State University as a National Merit Scholar and Space Science Fellowship Scholar. Mr. Greer also served as a legislative aide in the Texas House of Representatives and Senate.</p>
    <p>Mr. Greer is a visiting professor at Danube Valley University, Hungary and a former Adjunct Professor at Gulf Coast College of Law for International Commercial Arbitration and Arbitration Law. Mr. Greer also coached the domestic, international, and securities arbitration teams. Martin is conversational in Italian and English and maintains a working knowledge of Russian and Spanish. He is based in the Houston, Texas, office for Thornton, Reyes &amp; Vance, PLLC.</p>
  </div>
  <div class="abs" style="left:66px;top:589px">
    <div class="adm-title">ADMISSIONS TO PRACTICE</div>
    <ul class="adm-list">
      <li>Texas</li>
      <li>U.S. Northern, Western, and Southern Districts of Texas</li>
      <li>Fifth Circuit Court of Appeals</li>
      <li>Federal Circuit Court of Appeals</li>
    </ul>
  </div>
  <div class="abs page-num">01</div>

  <div class="abs photo" role="img" aria-label="Portrait of Daniel R. Vance in suit by office window" style="left:603px;top:103px;width:174px;height:165px;background:linear-gradient(160deg,#d9dde0,#3a3a3c)"></div>
  <div class="abs" style="left:605px;top:277px">
    <div class="name">Daniel R. Vance</div>
    <div class="role">III, J.D., Ph.D., Managing Member, Attorney</div>
    <div class="contact">
      <svg viewBox="0 0 10 9"><rect x="0" y="0" width="10" height="9" rx="1" fill="var(--orange)"/><path d="M1 2l4 3 4-3" stroke="#fff" fill="none" stroke-width="1"/></svg>
      <span>dvance@trv.law</span><span class="gap" style="width:6px"></span>
      <svg viewBox="0 0 10 9"><path d="M1 3c0-2 8-2 8 0v1H7V3H3v1H1z M2 5h6l1 4H1z" fill="var(--orange)"/></svg>
      <span>(713) 555-0142 x104</span>
    </div>
  </div>
  <div class="abs bio" style="left:822px;top:98px;width:243px;text-align:left;line-height:11.7px">
    <p>Representing a broad range of business clients, Daniel practices intellectual property law, residential &amp; commercial property law, commercial transactions, and litigation. He advises clients on business problems and solutions, entity design and creation, mergers and acquisitions, reorganizations, dispute resolution, and strategy. He is also heavily focused on intellectual property creation and protection, filing and obtaining hundreds of trademarks, domestic and internationally. Daniel was President of the Intellectual Property &amp; Technology Law Society, President of the Alternative Dispute Resolution Advocates, and was a member and coach of Gulf Coast College of Law's prestigious advocacy programs. Daniel also created and manages his own advertising implementation and optimization company. Daniel is licensed in all courts and federal districts of Texas and the U.S. Tax Court. He is based in the Houston, Texas, office.</p>
  </div>
  <div class="abs" style="left:822px;top:274px">
    <div class="adm-title">ADMISSIONS TO PRACTICE</div>
    <ul class="adm-list">
      <li>Texas</li>
      <li>U.S. Southern, Eastern, Northern, &amp; Western Districts of Texas</li>
      <li>US. Tax Court</li>
    </ul>
  </div>

  <div class="abs feature">
    <div class="abs photo" role="img" aria-label="Portrait of Lucas M. Reyes in three-piece suit seated in leather chair" style="left:40px;top:27px;width:174px;height:171px;background:linear-gradient(160deg,#4a5560,#1c1d20)"></div>
    <div class="abs" style="left:44px;top:216px">
      <div class="name">Lucas M. Reyes,</div>
      <div class="role">J.D., Senior Attorney, Business &amp; Litigation</div>
      <div class="mail-icon-row">
        <svg viewBox="0 0 10 9"><rect x="0" y="0" width="10" height="9" rx="1" fill="var(--orange)"/><path d="M1 2l4 3 4-3" stroke="#fff" fill="none" stroke-width="1"/></svg>
      </div>
      <div class="contact" style="margin-top:1px;padding-left:12px">
        <span>lreyes@trv.law</span><span class="gap"></span>
        <svg viewBox="0 0 10 9"><path d="M1 3c0-2 8-2 8 0v1H7V3H3v1H1z M2 5h6l1 4H1z" fill="var(--orange)"/></svg>
        <span>(713) 555-0142 x108</span>
      </div>
    </div>
    <div class="abs bio" style="left:269px;top:26px;width:246px">
      <p>Lucas Martin Reyes is a Senior Attorney with Thornton, Reyes &amp; Vance, PLLC. Lucas' practice focuses on construction litigation, and construction related disputes including residential &amp; commercial property law. In addition, he practices business &amp; corporate law, commercial transactions, litigation, complex business solutions, including entity creation, mergers, acquisitions, and reorganizations, as well as corporate strategy. Prior to joining Thornton, Reyes &amp; Vance, Mr. Reyes was a partner with Hollis &amp; Reyes focusing on construction, residential &amp; commercial property, and commercial transactions.</p>
      <p>Lucas completed his J.D. from Gulf Coast College of Law in 2011 and graduated from Brazos State University in 2005. Prior to working as an attorney, Lucas spent several years working in the construction industry, primarily in residential and commercial construction. Lucas is licensed to practice law in Texas and in the United States District Court for the Southern &amp; Eastern Districts of Texas. He is based in the Houston, Texas, office for Thornton, Reyes &amp; Vance, PLLC.</p>
    </div>
    <div class="abs" style="left:269px;top:248px">
      <div class="adm-title">ADMISSIONS TO PRACTICE:</div>
      <ul class="adm-list">
        <li>Texas</li>
        <li>U.S. Eastern and Southern Districts of Texas</li>
      </ul>
    </div>
  </div>
</div>
</body>
</html>
```